Business Card for IT company

I need a high tech looking business card using our logo. I prefer something clean and modern.

Target Market(s)

Buyers of IT hardware and software, IT Techies who are key influencers

Industry/Entity Type

Business

```html
<!DOCTYPE html>
<html lang="en">
<head>
<meta charset="utf-8">
<title>KVTR Consulting – Business Card</title>
<link rel="stylesheet" href="https://fonts.googleapis.com/css2?family=Montserrat:wght@500;600;700&family=Mulish:wght@400;600&display=swap">
<style>
  :root {
    --stage: #e8e3db;
    --ink: #222222;
    --charcoal: #333333;
    --green: #3f9e3f;
    --green-light: #6cbf45;
    --white: #ffffff;
    --muted: #444444;
  }
  * { margin: 0; padding: 0; box-sizing: border-box; }
  html, body { width: 1200px; height: 788px; overflow: hidden; }
  body {
    position: relative;
    background: var(--stage);
    font-family: "Mulish", Arial, sans-serif;
    color: var(--ink);
  }
  .side-label {
    position: absolute;
    width: 200px;
    text-align: center;
    font-family: Arial, Helvetica, sans-serif;
    font-size: 21px;
    color: var(--ink);
  }
  .card {
    position: absolute;
    width: 525px;
    height: 298px;
    border-radius: 18px;
    overflow: hidden;
  }
  .card--front { left: 43px; top: 70px; background: var(--white); }
  .card--back-green { left: 625px; top: 75px; background: radial-gradient(ellipse at 40% 30%, #58b048 0%, #6cbf45 70%, #73c447 100%); }
  .card--back-dark { left: 53px; top: 446px; background: #000; }
  .card--back-tech { left: 625px; top: 446px; background: #2a3f9a; }

  .texture, .artwork { position: absolute; inset: 0; }
  .texture {
    background:
      radial-gradient(ellipse at 12% 5%, rgba(120,120,120,.55) 0%, rgba(0,0,0,0) 35%),
      radial-gradient(ellipse at 85% 95%, rgba(170,150,160,.6) 0%, rgba(0,0,0,0) 40%),
      #050505;
  }
  .artwork {
    background:
      radial-gradient(ellipse at 50% 50%, #ffffff 0%, #e6f2ff 18%, #8fc4f2 38%, #4a6fd0 62%, #2b3a9a 85%, #243083 100%);
  }

  .wordmark {
    position: absolute;
    left: 0; right: 0;
    text-align: center;
    font-family: "Montserrat", Arial, sans-serif;
    font-weight: 600;
    line-height: 1;
  }
  .wordmark__name { display: block; font-size: 66px; letter-spacing: -2px; }
  .wordmark__tag { display: block; font-size: 20px; letter-spacing: 9px; margin-top: 8px; padding-left: 9px; }
  .wordmark--dark { color: var(--charcoal); }
  .wordmark--light { color: var(--white); }

  .card--front .wordmark { top: 64px; }
  .card--front .wordmark__name { font-size: 58px; }
  .card--front .wordmark__tag { font-size: 17px; letter-spacing: 8px; }

  .card--back-green .wordmark,
  .card--back-dark .wordmark,
  .card--back-tech .wordmark { top: 88px; }

  .web {
    position: absolute;
    left: 0; right: 0;
    bottom: 18px;
    text-align: center;
    font-family: "Montserrat", Arial, sans-serif;
    font-weight: 500;
    font-size: 18px;
    letter-spacing: 3px;
  }
  .web--dark { color: var(--charcoal); }
  .web--light { color: var(--white); }

  .person {
    position: absolute;
    top: 180px;
    right: 274px;
    text-align: right;
  }
  .person__name { font-family: "Montserrat", Arial, sans-serif; font-weight: 600; font-size: 17px; color: var(--green); }
  .person__role { font-size: 14px; color: var(--green); margin-top: 1px; }
  .divider {
    position: absolute;
    left: 263px; top: 183px;
    width: 1px; height: 36px;
    background: var(--muted);
  }
  .contact { font-size: 13.5px; color: var(--ink); }
  .contact b { font-weight: 600; }
  .contact--phone { position: absolute; left: 272px; top: 190px; }
  .address {
    position: absolute;
    left: 0; right: 0; top: 242px;
    text-align: center;
    font-size: 13.5px;
    color: var(--ink);
  }
  .band { position: absolute; left: 0; bottom: 0; width: 525px; height: 31px; }
  .band__text { position: absolute; bottom: 8px; font-size: 13.5px; color: var(--white); }
  .band__text--mobile { left: 60px; }
  .band__text--email { right: 66px; }
</style>
</head>
<body>
  <div class="side-label" style="left:220px; top:35px;">Front</div>
  <div class="side-label" style="left:795px; top:35px;">Back - 1</div>
  <div class="side-label" style="left:214px; top:405px;">Back - 2</div>
  <div class="side-label" style="left:795px; top:405px;">Back - 3</div>

  <section class="card card--front">
    <div class="wordmark wordmark--dark">
      <span class="wordmark__name">KVTR</span>
      <span class="wordmark__tag">CONSULTING</span>
    </div>
    <div class="person">
      <div class="person__name">Your Name</div>
      <div class="person__role">Designation</div>
    </div>
    <div class="divider"></div>
    <div class="contact contact--phone"><b>p</b> : +12 345 6789</div>
    <div class="address">#0000, Street Name, Area Name, Country</div>
    <svg class="band" viewBox="0 0 525 31" aria-hidden="true">
      <polygon points="0,0 233,0 251,31 0,31" fill="#5cb845"/>
      <polygon points="247,0 525,0 525,31 265,31" fill="#333333"/>
    </svg>
    <div class="band__text band__text--mobile"><b>c</b> : +12 345 6789</div>
    <div class="band__text band__text--email"><b>e</b> : info@kvtr.com</div>
  </section>

  <section class="card card--back-green">
    <div class="wordmark wordmark--dark">
      <span class="wordmark__name">KVTR</span>
      <span class="wordmark__tag">CONSULTING</span>
    </div>
    <div class="web web--dark">www.kvtr.com</div>
  </section>

  <section class="card card--back-dark">
    <div class="texture" role="img" aria-label="Dark metallic perforated dot texture with soft highlights"></div>
    <div class="wordmark wordmark--light">
      <span class="wordmark__name">KVTR</span>
      <span class="wordmark__tag">CONSULTING</span>
    </div>
    <div class="web web--light">www.kvtr.com</div>
  </section>

  <section class="card card--back-tech">
    <div class="artwork" role="img" aria-label="Glowing blue digital technology background with light rings, grid and binary code"></div>
    <div class="wordmark wordmark--dark">
      <span class="wordmark__name">KVTR</span>
      <span class="wordmark__tag">CONSULTING</span>
    </div>
    <div class="web web--dark">www.kvtr.com</div>
  </section>
</body>
</html>
```